Beauty Page

**UPDATED Brief**
We are looking for a website for a beauty organisation that targets both MEN & WOMAN. The focus of the company is in four main areas:

- Health
* Naturopathy & Remedial Massage
- Body
* Yoga
* Personal Training
* Massage
- Skin
* Skin care products such as Velmoracine
- Beauty
* Waxing
* Eye Treatments

We have attached the logo, (a sample of the website that I did - based on the book) and the sample of the pdf book
Updates

Dear All,

Thank you for your patience regarding the beauty contest. We were not happy with the designs that were submitted to us. We therefore had the Graphic designer to do the pricelist book to get all the colours for the organisation.

We are now happy to relaunch the contest and invite you all to take a look at the brief, download a sample of the book and the website we designed on what I’m looking for (the website is only a draft so I don’t want you to copy it) and let your creative mind go wild and present some suggestions to us.

Thanks

 

Target Market(s)

Woman & Men age 24 - 60

Industry/Entity Type

It Company

Requirements
Must have
• Use of main colours
Black
White
Gray - (CYMK - 65, 58, 57, 37)
Purpleish - Maroon (CYMK - 52, 69, 47, 25)

Use of the three color dots on the page.
(white, maroon & Gray)
Same fonts as the book
- Helvetica LT Std
Should not have
• Logo must not be altered i.e different colours, fonts, shadows etc...

```html
<!DOCTYPE html>
<html lang="en">
<head>
<meta charset="utf-8">
<title>Auralia &amp; Beauty — Health, Body &amp; Skin Care Centre</title>
<link rel="stylesheet" href="https://fonts.googleapis.com/css2?family=PT+Sans:wght@400;700&family=Italianno&display=swap">
<style>
:root{
  --maroon:#731c66;
  --maroon-dark:#5a1250;
  --maroon-light:#9a3a8c;
  --gray:#595959;
  --gray-mid:#8c8c8c;
  --gray-light:#d4d4d4;
  --panel:#f2f2f2;
  --white:#ffffff;
  --text:#444444;
  --muted:#a8a8a8;
}
*{margin:0;padding:0;box-sizing:border-box}
html,body{width:1200px;height:1078px;overflow:hidden}
body{
  position:relative;
  font-family:"PT Sans",Arial,sans-serif;
  color:var(--text);
  background:linear-gradient(180deg,#f7f7f7 0,#ededed 260px,#d9d9d9 560px,#cfcfcf 100%);
}
.abs{position:absolute}
.script{font-family:"Italianno",cursive}

/* top utility bar */
.utility{top:8px;left:633px;font-size:13px;font-weight:700;color:var(--maroon-dark)}
.checkout{top:8px;left:893px;font-size:13px;font-weight:700;color:var(--maroon-dark)}
.account{top:4px;left:1043px;width:141px;height:28px;border-radius:4px;
  background:linear-gradient(#fff,#ddd);border:1px solid #bbb;
  font-size:13px;font-weight:700;color:var(--maroon-dark);
  display:flex;align-items:center;justify-content:center;gap:8px}

/* location block */
.location{left:12px;top:42px;width:473px;height:216px;background:var(--maroon);border-radius:0 0 0 6px;color:var(--white)}
.location h2{position:absolute;left:10px;top:100px;font-size:23px;font-weight:700}
.location p{position:absolute;left:10px;font-size:17px;font-weight:700}
.location .addr{top:129px}
.location .phone{top:152px}
.location .more{position:absolute;right:22px;top:176px;font-size:26px;font-weight:700}
.brand{left:19px;top:12px;width:286px;height:116px;background:var(--white);border:2px solid #ccc;border-radius:8px;
  display:flex;align-items:center;gap:12px;padding-left:20px}
.brand-dot{width:22px;height:22px;background:var(--maroon);border-radius:50%}
.brand-name{font-size:30px;font-weight:700;color:var(--maroon)}

/* welcome */
.tagline{left:700px;top:34px;font-size:44px;color:var(--maroon);line-height:1}
.welcome{left:500px;top:62px;font-size:50px;color:var(--maroon);line-height:1}
.intro{left:502px;top:96px;width:690px;font-size:38px;line-height:37px;color:var(--maroon-dark)}

.follow{left:839px;top:216px;width:361px;height:38px;background:linear-gradient(90deg,#7f7f7f,#a5a5a5);
  display:flex;align-items:center;padding-left:70px;gap:10px}
.follow span{color:var(--white);font-size:20px;font-weight:700;margin-right:14px}
.follow i{width:22px;height:22px;background:var(--white);border-radius:3px;display:block}

/* navigation */
.nav{left:0;top:258px;width:1200px;height:110px;background:linear-gradient(180deg,#c9c9c9,#e9e9e9)}
.tab{position:absolute;top:12px;width:200px;height:100px}
.tab svg{position:absolute;inset:0}
.tab span{position:absolute;left:0;right:0;bottom:14px;text-align:center;color:var(--white);font-size:20px;font-weight:700;line-height:1.05}

/* hero */
.hero{left:12px;top:363px;width:1176px;height:190px;background:var(--white)}
.hero-photo{position:absolute;left:0;top:0;width:700px;height:190px;
  background:radial-gradient(ellipse at 30% 45%,#e86fb4 0,#f3a7d2 30%,#fbe3f0 60%,#ffffff 85%)}
.vip{position:absolute;left:703px;top:56px;width:469px;height:120px;background:var(--maroon);border-radius:8px 0 0 8px;color:var(--white);padding:6px 18px}
.vip p{font-size:40px;line-height:38px}
.vip small{position:absolute;right:14px;bottom:6px;font-size:13px;font-weight:700}

/* feature boxes */
.feature{top:563px;width:375px;height:222px;background:var(--panel);border-radius:6px;box-shadow:0 1px 3px rgba(0,0,0,.25)}
.feature-head{position:absolute;left:0;top:0;width:100%;height:26px;background:linear-gradient(90deg,#9a9a9a,#cfcfcf);border-radius:6px 6px 0 0}
.feature-title{position:absolute;left:40px;top:-6px;right:40px;height:32px;background:var(--maroon);
  clip-path:polygon(4% 0,96% 0,100% 100%,0 100%);color:var(--white);font-size:13px;font-weight:700;
  display:flex;align-items:center;justify-content:center;text-align:center;line-height:1.1}
.dots{position:absolute;left:24px;top:46px;display:flex;gap:8px}
.dots i{width:16px;height:16px;background:var(--maroon);border-radius:3px;display:block}
.dots i.g{background:var(--gray-mid)}
.learn{position:absolute;right:20px;top:42px;width:164px;height:26px;border-radius:13px;
  background:linear-gradient(#fff,#cfcfcf);border:1px solid #aaa;font-size:14px;font-weight:700;color:var(--maroon);
  display:flex;align-items:center;justify-content:center}
.player{position:absolute;left:16px;top:40px;width:343px;height:170px;background:linear-gradient(#dcdcdc,#bcbcbc)}
.product{position:absolute;background:linear-gradient(160deg,#ffffff,#d8d8e8 60%,#9eb0d8)}
.blurb{position:absolute;left:150px;top:96px;width:210px;font-size:12px;line-height:14px;color:var(--muted);font-weight:700}

/* bottom columns */
.column{top:792px;width:375px;height:204px;background:var(--white);border-radius:6px;padding:14px 18px;box-shadow:0 1px 3px rgba(0,0,0,.2)}
.column h3{font-size:19px;font-weight:700;color:var(--maroon);margin-bottom:10px}
.column p{font-size:13px;line-height:15px;color:var(--muted)}

.footer{left:12px;top:1031px;width:1176px;height:34px;background:var(--maroon);color:#c99bc0;font-size:14px;
  display:flex;align-items:center;justify-content:space-between;padding:0 18px}
</style>
</head>
<body>

<div class="abs utility">Your Cart is Empty.Currency AUD</div>
<div class="abs checkout">&#9656;Checkout Now</div>
<div class="abs account">My Account <span>&#9662;</span></div>

<section class="abs location">
  <h2>OUR LOCATION</h2>
  <p class="addr">Unit 4/72 Merrow Road Kestrel Vale, WA 6100</p>
  <p class="phone">Phone: (08) 9000 4127</p>
  <span class="more">Read More...</span>
</section>
<div class="abs brand"><i class="brand-dot"></i><span class="brand-name">Auralia &amp; Beauty</span></div>

<div class="abs tagline script">Health, Body &amp; Skin Care Centre</div>
<h1 class="abs welcome script">Welcome</h1>
<p class="abs intro script">Auralia &amp; Beauty is a health, massage, skincare centre that<br>provides quality treatments and education to each and every<br>client to cater for all individuals</p>

<div class="abs follow"><span>Follow us</span><i></i><i></i><i></i></div>

<nav class="abs nav">
  <div class="tab" style="left:86px">
    <svg viewBox="0 0 200 100" width="200" height="100"><polygon points="10,100 70,8 190,40 190,100" fill="#731c66"/><polygon points="70,8 120,22 80,44" fill="#ffffff" opacity=".85"/></svg>
    <span>Home</span></div>
  <div class="tab" style="left:356px">
    <svg viewBox="0 0 200 100" width="200" height="100"><polygon points="10,100 70,8 190,40 190,100" fill="#731c66"/><polygon points="70,8 120,22 80,44" fill="#ffffff" opacity=".85"/></svg>
    <span>About us</span></div>
  <div class="tab" style="left:640px">
    <svg viewBox="0 0 200 100" width="200" height="100"><polygon points="10,100 70,8 190,40 190,100" fill="#731c66"/><polygon points="70,8 120,22 80,44" fill="#ffffff" opacity=".85"/></svg>
    <span>Services<br>&amp; Treatments</span></div>
  <div class="tab" style="left:930px">
    <svg viewBox="0 0 200 100" width="200" height="100"><polygon points="10,100 70,8 190,40 190,100" fill="#731c66"/><polygon points="70,8 120,22 80,44" fill="#ffffff" opacity=".85"/></svg>
    <span>Contact us</span></div>
</nav>

<section class="abs hero">
  <div class="hero-photo" role="img" aria-label="Pink orchid flowers on a white background"></div>
  <div class="vip">
    <p class="script">Join Our Vip Club and learn Discounts on Products</p>
    <small>Read More...</small>
  </div>
</section>

<section class="abs feature" style="left:19px">
  <div class="feature-head"><div class="feature-title">Revolutionary New Treatments</div></div>
  <div class="player">
    <svg width="343" height="170" viewBox="0 0 343 170">
      <circle cx="171" cy="62" r="18" fill="#555"/><circle cx="171" cy="62" r="8" fill="#999"/>
      <rect x="0" y="140" width="343" height="30" fill="#e6e6e6"/>
      <circle cx="12" cy="155" r="6" fill="#555"/><circle cx="28" cy="155" r="6" fill="#555"/>
      <rect x="70" y="152" width="180" height="6" rx="3" fill="#555"/>
      <circle cx="76" cy="155" r="7" fill="#333"/>
      <polygon points="290,150 296,150 302,145 302,165 296,160 290,160" fill="#555"/>
      <path d="M314 149 L326 161 M326 149 L314 161" stroke="#555" stroke-width="3"/>
    </svg>
  </div>
</section>

<section class="abs feature" style="left:410px">
  <div class="feature-head"><div class="feature-title">Pure Dawn</div></div>
  <div class="dots"><i></i><i></i><i></i><i></i><i></i></div>
  <div class="learn">Learn More...</div>
  <div class="product" style="left:24px;top:84px;width:110px;height:126px" role="img" aria-label="Cleansing skincare bottles"></div>
  <p class="blurb">Trust Pure Dawn by Velmoracine to do good skin with clearing, soothing, refreshing ingredients that feel and smell great.</p>
</section>

<section class="abs feature" style="left:809px">
  <div class="feature-head"><div class="feature-title">Introducting our new product range<br>from Beauty Solara</div></div>
  <div class="dots"><i></i><i></i><i class="g"></i><i class="g"></i></div>
  <div class="learn">Learn More...</div>
  <div class="product" style="left:24px;top:84px;width:210px;height:120px" role="img" aria-label="Tubes and jar from the new skincare range"></div>
</section>

<section class="abs column" style="left:12px">
  <h3>Latest News</h3>
  <p>Cras neque justo, ultrices at, rhoncus a, facilisis eget,nisl. Quisque vitae pede. Nam et augue. Sed a elit. Ut vel massa. Suspendisse nibh pede, ultrices vitae, ultrices nec, mollis non, nibh. In sit amet pede quis leo vulputate hendrerit.Cras laoreet leo et justo auctor condimentum. Integer id enim. Suspendisse nibh pede, ultrices vitae, ultrices nec, mollis non, nibh.</p>
</section>
<section class="abs column" style="left:410px">
  <h3>Real Stories</h3>
  <p>Cras neque justo, ultrices at, rhoncus a, facilisis eget,nisl. Quisque vitae pede. Nam et augue. Sed a elit. Ut vel massa. Suspendisse nibh pede, ultrices vitae, ultrices nec, mollis non, nibh. In sit amet pede quis leo vulputate hendrerit.</p>
</section>
<section class="abs column" style="left:809px">
  <h3>What's hot?</h3>
  <p>Suspendisse nibh pede, ultrices vitae, ultrices nec, mollis non, nibh.<br><br>In sit amet pede quis leo vulputate hendrerit. Quisque vitae pede. Nam et augue. Sed a elit. Ut vel massa.Cras neque justo, ultrices at, rhoncus a, facilisis eget,nisl. Quisque vitae pede. Nam et augue. Sed a elit.</p>
</section>

<footer class="abs footer"><span>Copyright &copy;2011. All rights reserved.</span><span>Privacy Policy | Terms of use</span></footer>

</body>
</html>
```